Outdoor banner design for Physiotherapy Business

Hi
I need a design for a banner for my physiotherapy clinic. Our name is Tarvin Ridge Physiotherapy & Pilates, we have physiotherapy services, massage and we also run pilates classes. We need a banner, sized 1220mm X 2440mm.
The key ideas for our poster are the following:
- It should be easy to spot that it is about a physiotherapy and pilates clinic by people that are driving by;
- It should have our logo, address, phone number and website;
- It should contain the following text:
Suffering from frustrating pain or injury?
We can get you back to enjoying the pain-free, healthy life you've been missing.
I'm not to fussy about the colours used as long as it stands out and is easy to notice by people driving and walking by... But, I have attached some of our previous artwork so you can get an idea...

```html
<!DOCTYPE html>
<html lang="en">
<head>
<meta charset="utf-8">
<title>Tarvin Ridge Physiotherapy &amp; Pilates – Banner</title>
<link rel="stylesheet" href="https://fonts.googleapis.com/css2?family=Open+Sans:wght@300;400;600;700&display=swap">
<style>
  :root {
    --blue: #4c7bc4;
    --blue-deep: #2f57a4;
    --navy: #22386f;
    --grey: #7b7b7b;
    --white: #ffffff;
    --photo-warm: #c9a78e;
    --photo-cool: #cdd8e6;
  }
  * { margin: 0; padding: 0; box-sizing: border-box; }
  html, body { width: 1200px; height: 2400px; overflow: hidden; background: var(--white); }
  .banner {
    position: relative; width: 1200px; height: 2400px; overflow: hidden;
    font-family: "Open Sans", Arial, sans-serif; color: var(--blue);
  }
  .header-shape { position: absolute; left: 0; top: 0; }
  .headline { position: absolute; left: 0; top: 40px; width: 1200px; text-align: center; color: var(--white); }
  .headline .question { font-weight: 700; font-size: 35px; line-height: 1.2; }
  .headline .promise-light { font-weight: 300; font-size: 62px; line-height: 1.2; margin-top: 14px; }
  .headline .promise-strong { font-weight: 600; font-size: 48px; line-height: 1.62; }

  .photo {
    position: absolute; width: 432px; height: 432px; border-radius: 50%;
    border: 3px solid var(--blue); padding: 8px; background: var(--white);
  }
  .photo-fill { width: 100%; height: 100%; border-radius: 50%; }
  .photo-physio { left: 64px; top: 496px; }
  .photo-physio .photo-fill { background: linear-gradient(135deg, #efe6dc, var(--photo-warm) 60%, #2d3748); }
  .photo-pilates { left: 701px; top: 781px; }
  .photo-pilates .photo-fill { background: linear-gradient(160deg, #eef1f5, var(--photo-cool) 55%, #6c86b8); }
  .photo-massage { left: 64px; top: 1088px; }
  .photo-massage .photo-fill { background: linear-gradient(120deg, #5a3a28, var(--photo-warm) 55%, #e8cdb8); }
  .photo-work { left: 701px; top: 1424px; }
  .photo-work .photo-fill { background: linear-gradient(150deg, #f3f4f2, #d9dcd6 50%, #2b2f3a); }

  .service { position: absolute; font-weight: 700; font-size: 64px; line-height: 1; letter-spacing: 1px; color: var(--blue); }
  .service-left { left: 533px; }
  .service-right { right: 544px; text-align: right; }
  .rule { position: absolute; height: 0; border-top: 4px dotted var(--blue); }

  .brand {
    position: absolute; left: 0; top: 1880px; width: 1200px; text-align: center;
    font-weight: 700; font-size: 58px; line-height: 1.2; color: var(--blue);
  }
  .brand-mark {
    display: inline-block; width: 44px; height: 44px; border-radius: 50%;
    background: var(--blue); vertical-align: middle; margin-right: 20px; position: relative; top: -4px;
  }

  .address-bar {
    position: absolute; left: 0; top: 2099px; width: 1200px; height: 80px;
    background: var(--grey); color: var(--white); font-size: 35px; font-weight: 400;
    display: flex; align-items: center; justify-content: center;
  }
  .contact-band { position: absolute; left: 0; top: 2179px; width: 1200px; height: 221px; background: var(--navy); }
  .phone-line {
    position: absolute; left: 0; top: 22px; width: 1200px; text-align: center;
    color: var(--white); font-weight: 300;
  }
  .phone-line .label { font-size: 36px; }
  .phone-line .number { font-size: 98px; letter-spacing: 2px; margin-left: 10px; }
  .web-tab { position: absolute; left: 0; bottom: 0; }
  .web-address {
    position: absolute; left: 0; bottom: 14px; width: 1200px; text-align: center;
    font-weight: 700; font-size: 37px; color: var(--navy);
  }
</style>
</head>
<body>
<main class="banner">
  <svg class="header-shape" width="1200" height="500" viewBox="0 0 1200 500" aria-hidden="true">
    <defs>
      <linearGradient id="headerGradient" x1="0" y1="0" x2="1" y2="1">
        <stop offset="0" stop-color="#5b8ad0"/>
        <stop offset="1" stop-color="#2f57a4"/>
      </linearGradient>
    </defs>
    <path d="M0,250 C300,420 700,490 1200,390 L1200,300 C800,420 350,390 0,210 Z" fill="#2f57a4"/>
    <path d="M0,0 H1200 V330 C800,440 360,420 0,220 Z" fill="url(#headerGradient)"/>
    <path d="M0,225 C360,425 800,445 1200,335" fill="none" stroke="#ffffff" stroke-width="6"/>
  </svg>

  <header class="headline">
    <p class="question">Suffering from frustrating pain or injury?</p>
    <p class="promise-light">We can get you back to enjoying</p>
    <p class="promise-strong">the pain-free, healthy life<br>you've been missing.</p>
  </header>

  <div class="photo photo-physio"><div class="photo-fill" role="img" aria-label="Physiotherapist treating a patient's knee on a treatment table"></div></div>
  <div class="service service-left" style="top:612px">PHYSIOTHERAPY</div>
  <div class="rule" style="left:533px; right:10px; top:697px"></div>

  <div class="photo photo-pilates"><div class="photo-fill" role="img" aria-label="Women doing a pilates exercise on mats in a class"></div></div>
  <div class="service service-right" style="top:939px">PILATES</div>
  <div class="rule" style="left:8px; width:648px; top:1022px"></div>

  <div class="photo photo-massage"><div class="photo-fill" role="img" aria-label="Man lying face down receiving a back massage"></div></div>
  <div class="service service-left" style="top:1252px">MASSAGE</div>
  <div class="rule" style="left:533px; right:10px; top:1336px"></div>

  <div class="photo photo-work"><div class="photo-fill" role="img" aria-label="Office worker in a suit stretching his sore back at his desk"></div></div>
  <div class="service service-right" style="top:1558px; line-height:1.0">WORK<br>REHABILITATION</div>
  <div class="rule" style="left:8px; width:648px; top:1702px"></div>

  <div class="brand"><span class="brand-mark"></span>Tarvin Ridge<br>Physiotherapy &amp; Pilates</div>

  <div class="address-bar">Shop 12, 40 Harlow Street, Tarvin Ridge NSW 2299</div>

  <footer class="contact-band">
    <p class="phone-line"><span class="label">Call us:</span><span class="number">02 5550 1847</span></p>
    <svg class="web-tab" width="1200" height="90" viewBox="0 0 1200 90" aria-hidden="true">
      <path d="M230,90 C260,20 290,14 340,14 H860 C910,14 940,20 970,90 Z" fill="#ffffff"/>
    </svg>
    <p class="web-address">tarvinridgephysio.com.au</p>
  </footer>
</main>
</body>
</html>
```